Vorlen!

We need a packaging design for a new company based in Australia called "Vorlen".We require a packaging design for a new line of high quality socks we are selling. The socks come in black or white colours and in 3 different sizes. Small, Medium and Large.

The packaging design must be eye catching, classy and up market. The design must fit within the packaging.The design will be printed on a bag that looks like a zipper bag. (see attachment)The bag see through with matt finish. The package size is: Length 24cm (7.8 inches), height 12cm (3.9 inches). We would like to see designs that use the colours blue, red or purple.

Industry/Entity Type

It Company

Requirements
Must have
• The design must contain our company name "Vorlen " some where on the packaging with small font and web address. www.vorlen.com.au

```html
<!DOCTYPE html>
<html lang="en">
<head>
<meta charset="utf-8">
<title>Vorlen premium socks – packaging</title>
<link rel="stylesheet" href="https://fonts.googleapis.com/css2?family=Fredoka:wght@700&family=Open+Sans:wght@700;800&display=swap">
<style>
  :root {
    --stage: #8f8f8f;
    --bag: #d6d6d6;
    --bag-edge: #bdbdbd;
    --navy: #2b3282;
    --sky: #5aaed3;
    --brand-red: #e8202a;
    --white: #ffffff;
    --sock-light: #f4f4f4;
    --sock-shade: #dcdcdc;
    --zip: #f2f2f2;
  }
  html, body {
    margin: 0;
    padding: 0;
    width: 1200px;
    height: 1000px;
    overflow: hidden;
    background: var(--stage);
  }
  .canvas {
    position: relative;
    width: 1200px;
    height: 1000px;
  }
  .bag {
    position: absolute;
    left: 157px;
    top: 268px;
    width: 927px;
    height: 462px;
    background: var(--bag);
    box-shadow: inset 0 0 18px var(--bag-edge);
    overflow: hidden;
  }
  .sock-photo {
    position: absolute;
    left: 170px;
    top: 40px;
    width: 760px;
    height: 410px;
    border-radius: 48% 40% 44% 46% / 30% 40% 55% 50%;
    background: radial-gradient(ellipse at 55% 55%, var(--sock-light), var(--sock-shade));
    transform: rotate(6deg);
  }
  .zipper {
    position: absolute;
    left: 0;
    top: 12px;
    width: 100%;
    height: 18px;
    background: repeating-linear-gradient(90deg, var(--zip) 0 3px, transparent 3px 6px);
    border-top: 2px solid var(--white);
    border-bottom: 1px solid var(--bag-edge);
    z-index: 3;
  }
  .zipper-slider {
    position: absolute;
    left: 780px;
    top: 2px;
    width: 38px;
    height: 22px;
    background: var(--white);
    border-radius: 5px;
    z-index: 4;
  }
  .band-vertical {
    position: absolute;
    left: 104px;
    top: 0;
    width: 164px;
    height: 100%;
    background: linear-gradient(180deg, var(--navy) 0%, var(--navy) 55%, var(--sky) 100%);
    z-index: 1;
  }
  .band-horizontal {
    position: absolute;
    left: 0;
    top: 108px;
    width: 100%;
    height: 132px;
    background: linear-gradient(90deg, var(--navy) 0%, var(--navy) 45%, var(--sky) 100%);
    z-index: 2;
  }
  .tagline {
    position: absolute;
    left: 120px;
    top: 70px;
    margin: 0;
    font-family: "Open Sans", sans-serif;
    font-weight: 800;
    font-size: 15px;
    letter-spacing: 0.5px;
    color: var(--white);
    z-index: 3;
  }
  .brand-name {
    position: absolute;
    left: 22px;
    top: 118px;
    margin: 0;
    font-family: "Fredoka", sans-serif;
    font-weight: 700;
    font-size: 112px;
    line-height: 1;
    color: var(--brand-red);
    z-index: 3;
  }
  .size-label {
    position: absolute;
    left: 760px;
    top: 128px;
    width: 80px;
    text-align: center;
    font-family: "Open Sans", sans-serif;
    font-weight: 700;
    color: var(--white);
    z-index: 3;
  }
  .size-label .size-word {
    display: block;
    font-size: 17px;
  }
  .size-label .size-value {
    display: block;
    font-size: 58px;
    line-height: 1;
    font-weight: 800;
  }
  .web-address {
    position: absolute;
    right: 78px;
    bottom: 14px;
    margin: 0;
    font-family: "Open Sans", sans-serif;
    font-weight: 700;
    font-size: 14px;
    color: var(--navy);
    z-index: 3;
  }
</style>
</head>
<body>
<main class="canvas">
  <section class="bag">
    <div class="sock-photo" role="img" aria-label="Photo of a folded white ankle sock inside the bag"></div>
    <div class="zipper"></div>
    <div class="zipper-slider"></div>
    <div class="band-vertical"></div>
    <div class="band-horizontal"></div>
    <p class="tagline">premium socks</p>
    <h1 class="brand-name">VORLEN</h1>
    <div class="size-label">
      <span class="size-word">size</span>
      <span class="size-value">M</span>
    </div>
    <p class="web-address">www.vorlen.com.au</p>
  </section>
</main>
</body>
</html>
```